Fern Trader Supply Banners

We are looking for web banners that describe our business, we are an online shopping portal for businesses to buy natural and organic products direct form the manufacturers of those products.

1. Homepage banners (you can do 1 banner or up to 4 scrolling banners that describe the business. Width 780 * Height 235

This is where the hompage banner or banners will go.
http://www.ferntradersupply.example/

2. Banners to use on other websites 3 banners 250 x 250 120 x 300 300 x 90

Target Market(s)

The retail world, off the natural and organic product word, vegans, Gluten free, ext.

Industry/Entity Type

Online Shopping

Requirements
Must have
• Must match our site and tell our message well.

```html
<!DOCTYPE html>
<html lang="en">
<head>
<meta charset="utf-8">
<title>Fern Trader Supply Banners</title>
<link rel="stylesheet" href="https://fonts.googleapis.com/css2?family=Titillium+Web:wght@600;700&display=swap">
<style>
  :root {
    --canvas-bg: #c8c8c8;
    --brand-green: #4e9f24;
    --banner-white: #ffffff;
    --arrow-yellow: #f5c400;
    --ink: #1c1c1c;
    --placeholder: #d8ead0;
  }
  * { margin: 0; padding: 0; box-sizing: border-box; }
  html, body { width: 1200px; height: 819px; overflow: hidden; }
  body {
    background: var(--canvas-bg);
    font-family: "Titillium Web", sans-serif;
    position: relative;
  }
  .banner {
    position: absolute;
    background: var(--banner-white);
    box-shadow: 0 1px 1px rgba(0,0,0,0.15);
  }
  .banner__message {
    position: absolute;
    background: var(--brand-green);
    color: #fff;
    font-weight: 700;
    text-transform: uppercase;
  }
  .banner--skyscraper { left: 323px; top: 159px; width: 169px; height: 423px; }
  .banner--skyscraper .banner__message {
    left: 0; top: 0; width: 169px; height: 212px;
    padding: 33px 0 0 22px;
    font-size: 17px; line-height: 19.5px;
  }
  .banner--leaderboard { left: 535px; top: 336px; width: 423px; height: 127px; }
  .banner--leaderboard .banner__message {
    left: 0; top: 0; width: 210px; height: 127px;
    padding: 11px 0 0 14px;
    font-size: 16px; line-height: 19.5px;
  }
  .part { position: absolute; }
  .shop-icon svg, .flow-arrow svg { display: block; width: 100%; height: 100%; }
  .customer-portrait {
    background: linear-gradient(180deg, var(--brand-green) 0 30%, var(--placeholder) 30% 100%);
    border-radius: 40% 40% 45% 45%;
  }
  .wordmark {
    color: var(--brand-green);
    font-weight: 700;
    white-space: nowrap;
    line-height: 1;
  }
  .caption {
    position: absolute;
    left: 416px; top: 607px;
    color: var(--ink);
    font-weight: 600;
    font-size: 28px;
    line-height: 27px;
    text-transform: uppercase;
    letter-spacing: 0.2px;
  }
</style>
</head>
<body>

<section class="banner banner--skyscraper" aria-label="Banner 120 by 300">
  <p class="banner__message">The best<br>marketplace<br>for all the<br>natural<br>products<br>for buyers &amp;<br>sellers</p>

  <div class="part shop-icon" style="left:55px;top:224px;width:56px;height:44px;">
    <svg viewBox="0 0 56 44" aria-hidden="true">
      <path d="M6 0h44l6 14H0z" fill="var(--brand-green)"/>
      <path d="M10 3h4l-2 10h-5zM20 3h4l-1 10h-5zM32 3h4l1 10h-5zM42 3h4l3 10h-5z" fill="#fff"/>
      <rect x="0" y="14" width="56" height="5" rx="2.5" fill="var(--brand-green)"/>
      <rect x="4" y="22" width="48" height="22" fill="var(--brand-green)"/>
    </svg>
  </div>

  <div class="part flow-arrow" style="left:15px;top:226px;width:43px;height:63px;">
    <svg viewBox="0 0 43 63" aria-hidden="true">
      <path d="M42 4 C22 8 12 22 14 44" fill="none" stroke="var(--arrow-yellow)" stroke-width="5" stroke-linecap="round"/>
      <path d="M4 42 L14 62 L24 42 Z" fill="var(--arrow-yellow)"/>
    </svg>
  </div>

  <div class="part wordmark" style="left:17px;top:308px;font-size:16px;">Fern Trader Supply</div>

  <div class="part customer-portrait" role="img" aria-label="Illustrated buyer" style="left:68px;top:360px;width:34px;height:48px;"></div>

  <div class="part flow-arrow" style="left:114px;top:346px;width:43px;height:63px;">
    <svg viewBox="0 0 43 63" aria-hidden="true">
      <path d="M2 60 C22 54 30 40 29 20" fill="none" stroke="var(--arrow-yellow)" stroke-width="5" stroke-linecap="round"/>
      <path d="M19 22 L29 2 L39 22 Z" fill="var(--arrow-yellow)"/>
    </svg>
  </div>
</section>

<section class="banner banner--leaderboard" aria-label="Banner 300 by 90">
  <p class="banner__message">The best market-<br>place for all the<br>natural products<br>for buyers &amp;<br>sellers</p>

  <div class="part shop-icon" style="left:221px;top:10px;width:43px;height:35px;">
    <svg viewBox="0 0 56 44" aria-hidden="true">
      <path d="M6 0h44l6 14H0z" fill="var(--brand-green)"/>
      <path d="M10 3h4l-2 10h-5zM20 3h4l-1 10h-5zM32 3h4l1 10h-5zM42 3h4l3 10h-5z" fill="#fff"/>
      <rect x="0" y="14" width="56" height="5" rx="2.5" fill="var(--brand-green)"/>
      <rect x="4" y="22" width="48" height="22" fill="var(--brand-green)"/>
    </svg>
  </div>

  <div class="part flow-arrow" style="left:336px;top:13px;width:59px;height:50px;">
    <svg viewBox="0 0 59 50" aria-hidden="true">
      <path d="M56 48 C52 28 38 14 18 12" fill="none" stroke="var(--arrow-yellow)" stroke-width="5" stroke-linecap="round"/>
      <path d="M20 2 L1 12 L20 22 Z" fill="var(--arrow-yellow)"/>
    </svg>
  </div>

  <div class="part wordmark" style="left:258px;top:53px;font-size:12px;">Fern Trader Supply</div>

  <div class="part flow-arrow" style="left:238px;top:68px;width:62px;height:45px;">
    <svg viewBox="0 0 62 45" aria-hidden="true">
      <path d="M3 2 C5 20 20 32 42 34" fill="none" stroke="var(--arrow-yellow)" stroke-width="5" stroke-linecap="round"/>
      <path d="M40 24 L61 35 L40 44 Z" fill="var(--arrow-yellow)"/>
    </svg>
  </div>

  <div class="part customer-portrait" role="img" aria-label="Illustrated buyer" style="left:379px;top:69px;width:34px;height:48px;"></div>
</section>

<p class="caption">Pls check the animation<br>for each one of the banners<br>they are all the same.</p>

</body>
</html>
```